Job advert for Forged by Circle

I would like a poster graphic that I can promote on social media to advertise a job vacancy we will be promoting our upcoming jobs, here is the text...

WE ARE ON THE…

LOOKOUT
(maybe insert graphic or icon that fits with the message here)

For A

OPERATIONS AND HR MANAGER

MEMBERSHIP ADVISOR (EAST MIDLANDS)

SOCIAL MEDIA CONTENT CREATOR

THE UK’s FASTEST GROWING NETWORK FOR MANUFACTURERS

OFFICES IN BIRMINGHAM AND LEEDS - WE ARE AN INCLUSIVE EMPLOYER (use the equality logo provided here)

Target Market(s)

people looking to find a new job

Industry/Entity Type

Manufacture

Font styles to use
Sans Serif

Colors
f04a50
f68e4e
e667a6

Requirements
Must have
• Clear simple and contemporary style
Nice to have
• a nice graphic or icon to convey the text message
Should not have
• use of dark depressing colours

```html
<!DOCTYPE html>
<html lang="en">
<head>
<meta charset="utf-8">
<title>Forged by Circle – We Are On The Lookout</title>
<link href="https://fonts.googleapis.com/css2?family=Graduate&family=Open+Sans:wght@300;400;600&display=swap" rel="stylesheet">
<style>
  :root {
    --page-bg: #e9ebec;
    --sky-top: #3fb3d8;
    --sky-mid: #8fd6ea;
    --sky-low: #5fb4d4;
    --sky-foot: #c9eaf4;
    --ink-dark: #1f2340;
    --lookout-blue: #3a56a8;
    --band: #7f96c9;
    --rule: rgba(40, 60, 90, 0.35);
    --white: #ffffff;
    --yorkshire-green: #a6cf2a;
    --pledge-grey: #5d5d66;
    --pledge-orange: #f68e4e;
    --midlands-red: #f04a50;
  }
  * { margin: 0; padding: 0; box-sizing: border-box; }
  html, body { width: 1200px; height: 1200px; overflow: hidden; }
  body {
    background: var(--page-bg);
    font-family: "Open Sans", sans-serif;
    position: relative;
  }
  .poster {
    position: absolute;
    left: 220px; top: 30px;
    width: 760px; height: 1140px;
    overflow: hidden;
    background:
      radial-gradient(ellipse 60% 35% at 50% 62%, rgba(255,255,255,0.55), transparent 70%),
      linear-gradient(180deg, var(--sky-top) 0%, var(--sky-mid) 45%, var(--sky-low) 72%, var(--sky-foot) 100%);
  }
  .photo-cluster { position: absolute; inset: 0; }
  .headline {
    position: absolute; top: 556px; width: 100%;
    text-align: center;
    font-weight: 600; font-size: 39px; letter-spacing: -0.5px;
    color: var(--ink-dark);
  }
  .lookout {
    position: absolute; top: 592px; width: 100%;
    text-align: center;
    font-family: "Graduate", sans-serif;
    font-size: 82px; letter-spacing: 2px;
    color: var(--lookout-blue);
  }
  .for-a {
    position: absolute; top: 706px; width: 100%;
    text-align: center; font-size: 20px; color: var(--ink-dark);
  }
  .vacancies {
    position: absolute; top: 745px; left: 50%; transform: translateX(-50%);
    width: 445px; list-style: none;
  }
  .vacancies li {
    text-align: center; font-weight: 600; font-size: 21px;
    color: var(--ink-dark); line-height: 35px; white-space: nowrap;
  }
  .vacancies li + li { border-top: 1px solid var(--rule); }
  .info-band {
    position: absolute; top: 876px; width: 100%; height: 75px;
    background: var(--band);
    display: flex; flex-direction: column; justify-content: center; align-items: center;
    color: var(--white); font-size: 17px; line-height: 25px; font-weight: 400;
  }
  .logo-row {
    position: absolute; top: 1000px; width: 100%; height: 90px;
    display: flex; align-items: center; justify-content: space-between;
    padding: 0 70px;
  }
  .brand-mark { display: flex; align-items: center; gap: 8px; }
  .brand-mark .dot { border-radius: 50%; flex: none; }
  .brand-yorkshire { color: var(--yorkshire-green); font-size: 13px; font-weight: 400; line-height: 13px; }
  .brand-yorkshire .dot { width: 40px; height: 40px; background: var(--yorkshire-green); }
  .brand-pledge { color: var(--pledge-grey); font-size: 28px; font-weight: 400; line-height: 27px; }
  .brand-pledge .dot { width: 92px; height: 92px; background: var(--pledge-orange); margin-right: 4px; }
  .brand-midlands { color: var(--midlands-red); font-size: 13px; font-weight: 400; line-height: 13px; }
  .brand-midlands .dot { width: 40px; height: 40px; background: var(--midlands-red); }
</style>
</head>
<body>
  <main class="poster">
    <svg class="photo-cluster" width="760" height="1140" viewBox="0 0 760 1140">
      <defs>
        <linearGradient id="desk-tones" x1="0" y1="0" x2="1" y2="1">
          <stop offset="0" stop-color="#b89a78"/>
          <stop offset="0.5" stop-color="#e6e8ea"/>
          <stop offset="1" stop-color="#7f9fb8"/>
        </linearGradient>
        <linearGradient id="team-tones" x1="0" y1="0" x2="0" y2="1">
          <stop offset="0" stop-color="#5d96c8"/>
          <stop offset="0.55" stop-color="#2c3e55"/>
          <stop offset="1" stop-color="#0f1620"/>
        </linearGradient>
        <linearGradient id="workforce-tones" x1="0" y1="0" x2="0" y2="1">
          <stop offset="0" stop-color="#dfe4e8"/>
          <stop offset="0.5" stop-color="#8a7a6e"/>
          <stop offset="1" stop-color="#3c4a6a"/>
        </linearGradient>
      </defs>
      <g class="orbit-lines" fill="none" stroke="var(--white)" stroke-opacity="0.7" stroke-width="1.5">
        <circle cx="375" cy="276" r="248"/>
        <circle cx="624" cy="406" r="196"/>
        <circle cx="212" cy="428" r="118"/>
      </g>
      <circle cx="375" cy="276" r="222" fill="var(--white)"/>
      <circle cx="375" cy="276" r="185" fill="url(#desk-tones)" role="img" aria-label="Photo of a hand typing on a laptop at a desk"/>
      <circle cx="624" cy="406" r="170" fill="var(--white)"/>
      <circle cx="624" cy="406" r="147" fill="url(#team-tones)" role="img" aria-label="Photo of a line of business professionals standing with arms folded"/>
      <circle cx="212" cy="428" r="103" fill="var(--white)"/>
      <circle cx="212" cy="428" r="89" fill="url(#workforce-tones)" role="img" aria-label="Photo of a diverse group of workers from different trades"/>
    </svg>

    <h1 class="headline">WE ARE ON THE...</h1>
    <p class="lookout">LOOKOUT</p>
    <p class="for-a">For a</p>
    <ul class="vacancies">
      <li>OPERATIONS AND HR MANAGER</li>
      <li>MEMBERSHIP ADVISOR (EAST MIDLANDS)</li>
      <li>SOCIAL MEDIA CONTENT CREATOR</li>
    </ul>

    <div class="info-band">
      <span>The Uk’s Fastest Growing Network For Manufacturers</span>
      <span>Offices In Birmingham And Leeds - We Are An Inclusive Employer.</span>
    </div>

    <div class="logo-row">
      <div class="brand-mark brand-yorkshire"><span class="dot"></span><span>FORGED BY CIRCLE<br>YORKSHIRE</span></div>
      <div class="brand-mark brand-pledge"><span class="dot"></span><span>open door<br>pledge</span></div>
      <div class="brand-mark brand-midlands"><span class="dot"></span><span>FORGED BY CIRCLE<br>MIDLANDS</span></div>
    </div>
  </main>
</body>
</html>
```